New Business Card Design

We would like to refresh our business cards and make them look better. We are an IT company specialising in Cloud Services, IT Managed Services, software and hardware. I have attached a PSD of our current design. Also attached our logo.
Updates

I have uploaded all new logos in EPS format.

Can you please edit all designs to include a job title for Marcus Penn, eg. General Manager

Industry/Entity Type

Software

Colors
ffffff

Requirements
Must have
• Please use white background.
Should not have
• Black background

```html
<!DOCTYPE html>
<html lang="en">
<head>
<meta charset="utf-8">
<title>Meridian Systems – Business Card</title>
<link href="https://fonts.googleapis.com/css2?family=Jost:wght@400;500;700&display=swap" rel="stylesheet">
<style>
  :root {
    --stage: #ecebe8;
    --card-white: #ffffff;
    --brand-red: #bf3a2b;
    --brand-red-light: #cb4a38;
    --brand-red-dark: #a8301f;
    --ink-dark: #3a3a3c;
    --label-dark: #5a1a10;
    --shadow: rgba(0, 0, 0, 0.18);
  }
  * { box-sizing: border-box; margin: 0; padding: 0; }
  html, body {
    width: 1200px; height: 1200px; overflow: hidden;
    background: var(--stage);
    font-family: "Jost", "Futura", sans-serif;
  }
  .stage {
    position: relative; width: 1200px; height: 1200px;
    display: flex; flex-direction: column; align-items: center; justify-content: center; gap: 60px;
  }
  .card {
    position: relative; width: 820px; height: 500px; overflow: hidden;
    box-shadow: 0 12px 30px var(--shadow);
  }
  /* Front */
  .card-front { background: var(--card-white); }
  .front-website {
    position: absolute; top: 34px; right: 40px;
    color: var(--brand-red); font-size: 25px; font-weight: 500; letter-spacing: 1.5px;
  }
  .brand {
    position: absolute; left: 70px; top: 150px;
    display: flex; align-items: center; gap: 22px;
  }
  .brand-dot { width: 70px; height: 70px; border-radius: 50%; background: var(--brand-red); }
  .brand-name {
    color: var(--ink-dark); font-size: 48px; font-weight: 400; letter-spacing: 6px; line-height: 1;
  }
  .front-band {
    position: absolute; left: 0; right: 0; bottom: 0; height: 190px;
    background: var(--brand-red);
  }
  .holder {
    position: absolute; right: 40px; top: 22px; text-align: right;
  }
  .holder-name { color: #fff; font-size: 30px; font-weight: 700; letter-spacing: 1px; }
  .holder-title { color: var(--label-dark); font-size: 16px; font-weight: 500; margin-top: 2px; }
  .contacts {
    position: absolute; right: 40px; bottom: 34px;
    display: flex; gap: 26px; color: #fff; font-size: 21px;
  }
  .contact-label { color: var(--label-dark); font-weight: 700; margin-right: 6px; }
  /* Back */
  .card-back { background: var(--brand-red); }
  .back-pattern {
    position: absolute; inset: 0;
    background: radial-gradient(ellipse at 60% 45%, var(--brand-red-light), var(--brand-red) 70%);
  }
  .back-tagline {
    position: absolute; right: 40px; top: 205px;
    color: #fff; font-size: 25px; font-weight: 400; letter-spacing: 0.5px;
  }
</style>
</head>
<body>
<main class="stage">
  <section class="card card-front" aria-label="Business card front">
    <div class="front-website">www.meridianit.com.au</div>
    <div class="brand">
      <span class="brand-dot"></span>
      <span class="brand-name">meridian systems</span>
    </div>
    <div class="front-band">
      <div class="holder">
        <div class="holder-name">Marcus Penn</div>
        <div class="holder-title">General Manager</div>
      </div>
      <div class="contacts">
        <span><span class="contact-label">P</span>07 3000 1234</span>
        <span><span class="contact-label">M</span>0400 555 218</span>
        <span><span class="contact-label">E</span>mpenn@meridianit.com.au</span>
      </div>
    </div>
  </section>

  <section class="card card-back" aria-label="Business card back">
    <div class="back-pattern" role="img" aria-label="Faint embossed oval dot pattern in tones of red"></div>
    <div class="back-tagline">IT SERVICES • SOLUTIONS • SUPPORT</div>
  </section>
</main>
</body>
</html>
```